Swimming Pool Supply Company Business Cards

We need business cards designed for company. These need to be easy to edit so that we can fill in names, titles, and contact info for each person who works here.

Dalton R. Whitfield
Manager of Legal & Finance
K.L. Brisbane, Incorporated

4837 Grenway Avenue
Marlow Heights, PA 19243

E. dalton@klbrisbane-example.com
M. (215) 555-0173
O. (215) 555-0148

Contact Information for Business Card

Looking to upgrade current business cards with graphic that can be edited. Looking for fresh ideas for an age old industry.

Font styles to use
Serif
Sans Serif

Colors

Designer to choose colors to be used in the design.

Requirements
Must have
• Professional, fresh, unique but professional

```html
<!DOCTYPE html>
<html lang="en">
<head>
<meta charset="utf-8">
<title>K.L. Brisbane — Business Cards</title>
<link rel="stylesheet" href="https://fonts.googleapis.com/css2?family=Cinzel:wght@400&family=Lato:wght@400&display=swap">
<style>
  :root {
    --backdrop: #4a4a4a;
    --card-light: #ffffff;
    --card-dark: #1f1d1e;
    --ink-dark: #141414;
    --ink-light: #ffffff;
  }
  * { margin: 0; padding: 0; box-sizing: border-box; }
  html, body {
    width: 1200px; height: 1200px; overflow: hidden;
    background: var(--backdrop);
  }
  .canvas { position: relative; width: 1200px; height: 1200px; }
  .card {
    position: absolute; top: 310px; width: 364px; height: 594px;
    display: flex; flex-direction: column; align-items: center;
    font-family: "Lato", sans-serif;
  }
  .card--front { left: 234px; background: var(--card-light); color: var(--ink-dark); }
  .card--back { left: 627px; width: 369px; background: var(--card-dark); color: var(--ink-light); }

  .brand {
    display: flex; align-items: center; gap: 14px;
    font-family: "Lato", sans-serif; font-weight: 400;
    font-size: 44px; letter-spacing: 2px; line-height: 1;
  }
  .brand__dot { width: 22px; height: 22px; border-radius: 50%; background: currentColor; }
  .card--front .brand { margin-top: 144px; }
  .card--back .brand { margin-top: 268px; }

  .contact { margin-top: 126px; text-align: center; width: 226px; }
  .contact__name { font-size: 21px; letter-spacing: 0.5px; line-height: 1.1; }
  .contact__line { font-size: 16px; line-height: 21px; }
  .contact__rule { height: 1px; background: var(--ink-dark); margin: 13px auto; width: 212px; }
  .contact__address .contact__line { font-size: 16.5px; }

  .tagline {
    margin-top: 168px; text-align: center;
    font-family: "Cinzel", serif; font-size: 17.5px; letter-spacing: 0.8px;
    line-height: 32px;
  }
</style>
</head>
<body>
<main class="canvas">
  <section class="card card--front">
    <div class="brand"><span class="brand__dot"></span><span class="brand__name">BRISBANE</span></div>
    <div class="contact">
      <p class="contact__name">DALTON R. WHITFIELD</p>
      <p class="contact__line">Manager of Legal &amp; Finance</p>
      <p class="contact__line">K.L. Brisbane, Incorporated</p>
      <div class="contact__rule"></div>
      <div class="contact__address">
        <p class="contact__line">4837 Grenway Avenue</p>
        <p class="contact__line">Marlow Heights, PA 19243</p>
      </div>
      <div class="contact__rule"></div>
      <p class="contact__line">M: (215) 555-0173</p>
      <p class="contact__line">P: (215) 555-0148</p>
    </div>
  </section>

  <section class="card card--back">
    <div class="brand"><span class="brand__dot"></span><span class="brand__name">BRISBANE</span></div>
    <p class="tagline">BIG ENOUGH TO SERVE YOU<br>SMALL ENOUGH TO CARE</p>
  </section>
</main>
</body>
</html>
```